banner ad

We're looking for a banner similar to the one shown on the attached file. The same 4 keywords, the same text up top, but with new formatting, design and perhaps color scheme. Looking for something to catch people's attention that will stand out on this particular page shown in the attached image. Our goal is to find a banner with a better click through rate than the current version.

```html
<!DOCTYPE html>
<html lang="en">
<head>
<meta charset="utf-8">
<title>Ads Related to blood glucose</title>
<link rel="stylesheet" href="https://fonts.googleapis.com/css2?family=Arimo:wght@400;700&display=swap">
<style>
  :root {
    --header-bg: #0f2a47;
    --header-text: #ffffff;
    --label-text: #9fb6cf;
    --label-ring: #3b5878;
    --panel: #f3f7fb;
    --cta-start: #ff9a1f;
    --cta-end: #ff5a36;
    --cta-text: #ffffff;
    --cta-shadow: rgba(214, 74, 20, 0.35);
    --icon-bg: #ffffff;
    --icon-fg: #ff6a2e;
    --accent-strip: #ff7a29;
  }
  * { margin: 0; padding: 0; box-sizing: border-box; }
  html, body {
    width: 1200px;
    height: 263px;
    overflow: hidden;
    background: var(--panel);
    font-family: "Arimo", Arial, sans-serif;
  }
  .ad-banner {
    position: relative;
    width: 1200px;
    height: 263px;
    background: var(--panel);
  }
  .ad-header {
    height: 55px;
    background: var(--header-bg);
    display: flex;
    align-items: center;
    justify-content: space-between;
    padding: 0 22px;
  }
  .ad-title {
    color: var(--header-text);
    font-size: 28px;
    font-weight: 400;
    letter-spacing: 0.2px;
  }
  .ad-label {
    color: var(--label-text);
    font-size: 13px;
    letter-spacing: 1.5px;
    border: 1px solid var(--label-ring);
    border-radius: 12px;
    padding: 4px 12px;
  }
  .keyword-row {
    position: absolute;
    top: 87px;
    left: 30px;
    right: 30px;
    display: flex;
    justify-content: space-between;
  }
  .keyword-card {
    width: 270px;
    height: 112px;
    border-radius: 16px;
    background: linear-gradient(135deg, var(--cta-start) 0%, var(--cta-end) 100%);
    box-shadow: 0 8px 18px var(--cta-shadow);
    display: flex;
    align-items: center;
    justify-content: space-between;
    gap: 12px;
    padding: 0 18px 0 22px;
    color: var(--cta-text);
    text-decoration: none;
  }
  .keyword-text {
    font-size: 19px;
    font-weight: 700;
    line-height: 1.25;
    text-transform: uppercase;
    letter-spacing: 0.3px;
  }
  .keyword-icon {
    flex: 0 0 42px;
    width: 42px;
    height: 42px;
    border-radius: 50%;
    background: var(--icon-bg);
    display: flex;
    align-items: center;
    justify-content: center;
  }
  .keyword-icon svg { width: 20px; height: 20px; }
  .accent-strip {
    position: absolute;
    left: 0;
    right: 0;
    bottom: 0;
    height: 8px;
    background: linear-gradient(90deg, var(--cta-start), var(--cta-end));
  }
</style>
</head>
<body>
  <section class="ad-banner">
    <header class="ad-header">
      <h1 class="ad-title">Ads Related to blood glucose</h1>
      <span class="ad-label">ADVERTISEMENT</span>
    </header>
    <nav class="keyword-row">
      <a class="keyword-card" href="#">
        <span class="keyword-text">Blood Glucose</span>
        <span class="keyword-icon"><svg viewBox="0 0 20 20" aria-hidden="true"><path d="M4 10h11M10 4.5l5.5 5.5-5.5 5.5" fill="none" stroke="#ff6a2e" stroke-width="2.6" stroke-linecap="round" stroke-linejoin="round"/></svg></span>
      </a>
      <a class="keyword-card" href="#">
        <span class="keyword-text">Normal Blood<br>Sugar Range</span>
        <span class="keyword-icon"><svg viewBox="0 0 20 20" aria-hidden="true"><path d="M4 10h11M10 4.5l5.5 5.5-5.5 5.5" fill="none" stroke="#ff6a2e" stroke-width="2.6" stroke-linecap="round" stroke-linejoin="round"/></svg></span>
      </a>
      <a class="keyword-card" href="#">
        <span class="keyword-text">Blood Sugar<br>Levels Chart</span>
        <span class="keyword-icon"><svg viewBox="0 0 20 20" aria-hidden="true"><path d="M4 10h11M10 4.5l5.5 5.5-5.5 5.5" fill="none" stroke="#ff6a2e" stroke-width="2.6" stroke-linecap="round" stroke-linejoin="round"/></svg></span>
      </a>
      <a class="keyword-card" href="#">
        <span class="keyword-text">What Is Normal<br>Blood Sugar?</span>
        <span class="keyword-icon"><svg viewBox="0 0 20 20" aria-hidden="true"><path d="M4 10h11M10 4.5l5.5 5.5-5.5 5.5" fill="none" stroke="#ff6a2e" stroke-width="2.6" stroke-linecap="round" stroke-linejoin="round"/></svg></span>
      </a>
    </nav>
    <div class="accent-strip"></div>
  </section>
</body>
</html>
```